Best in class business looking for best in class stationery that accurately reflects the brand image we are trying to build as the brand expands throughout the country. The Varying items should be an eye catching design that makes even the simplest letter or small business card stand out in the crowd.

Target Market(s)

Professionals

Industry/Entity Type

Real Estate

Other font styles liked:
• See atttached logo

Requirements
Must have
• Letterhead
• Business cards
• Envelopes
• Labels for larger mailings
Nice to have
• Folders
• Notebook
Should not have
• Stale design elements

```html
<!DOCTYPE html>
<html lang="en">
<head>
<meta charset="utf-8">
<title>Ridgeline Property Group — Business Card</title>
<link rel="stylesheet" href="https://fonts.googleapis.com/css2?family=Cinzel:wght@400;500&family=Open+Sans:wght@400;600&display=swap">
<style>
  :root {
    --page: #e9e6e1;
    --navy: #2b3990;
    --navy-deep: #23307c;
    --stripe: #3d5fbf;
    --paper: #ffffff;
    --ink-soft: #4a56a0;
    --white: #ffffff;
  }
  * { box-sizing: border-box; margin: 0; padding: 0; }
  html, body {
    width: 1200px;
    height: 1023px;
    overflow: hidden;
    background: var(--page);
  }
  .canvas {
    position: relative;
    width: 1200px;
    height: 1023px;
  }
  .card {
    position: absolute;
    width: 640px;
    height: 366px;
    overflow: hidden;
    box-shadow: 0 10px 28px rgba(0,0,0,0.18);
  }
  .card-front { left: 60px; top: 90px; background: var(--paper); }
  .card-back  { left: 500px; top: 567px; background: var(--navy); }

  .roof-band { position: absolute; inset: 0; }

  .brand {
    position: absolute;
    font-family: "Cinzel", serif;
    font-weight: 400;
    color: var(--navy);
    line-height: 1;
  }
  .card-front .brand { left: 48px; top: 58px; }
  .brand-name { font-size: 25px; letter-spacing: 0.5px; display: flex; align-items: center; gap: 10px; white-space: nowrap; }
  .brand-mark { width: 12px; height: 12px; background: currentColor; display: inline-block; }
  .brand-sub {
    margin-top: 7px;
    font-size: 11px;
    letter-spacing: 7px;
    padding-left: 98px;
    border-top: 1px solid currentColor;
    padding-top: 6px;
    width: 300px;
  }

  .person { position: absolute; left: 48px; top: 160px; font-family: "Cinzel", serif; color: var(--ink-soft); }
  .person-name { font-size: 22px; letter-spacing: 0.5px; white-space: nowrap; }
  .person-role { font-family: "Open Sans", sans-serif; font-size: 12px; margin-top: 4px; }

  .contact { position: absolute; left: 48px; top: 250px; list-style: none;
    font-family: "Open Sans", sans-serif; font-size: 13px; color: var(--ink-soft); }
  .contact li { display: flex; align-items: center; gap: 8px; height: 21px; white-space: nowrap; }
  .contact svg { width: 12px; height: 12px; fill: var(--ink-soft); }

  .address { position: absolute; left: 518px; top: 148px; font-style: normal; white-space: nowrap;
    font-family: "Open Sans", sans-serif; font-size: 12px; line-height: 18px; color: var(--ink-soft); }

  .stripes { position: absolute; inset: 0; }
  .card-back .brand { color: var(--white); left: 250px; top: 160px; }
  .card-back .brand-name { font-size: 28px; }
  .card-back .brand-sub { width: 330px; padding-left: 112px; font-size: 12px; }
</style>
</head>
<body>
<main class="canvas">

  <section class="card card-front" aria-label="Business card front">
    <svg class="roof-band" viewBox="0 0 640 366" aria-hidden="true">
      <polygon points="384,0 408,0 500,183 408,366 384,366 476,183" fill="var(--navy)"/>
    </svg>

    <div class="brand">
      <div class="brand-name">Ridgeline Property</div>
      <div class="brand-sub">Group</div>
    </div>

    <div class="person">
      <div class="person-name">Marcus Hale</div>
      <div class="person-role">Director</div>
    </div>

    <ul class="contact">
      <li>
        <svg viewBox="0 0 24 24"><path d="M6.6 10.8a15 15 0 0 0 6.6 6.6l2.2-2.2c.3-.3.7-.4 1-.2 1.1.4 2.3.6 3.6.6.6 0 1 .4 1 1V20c0 .6-.4 1-1 1A17 17 0 0 1 3 4c0-.6.4-1 1-1h3.5c.6 0 1 .4 1 1 0 1.3.2 2.5.6 3.6.1.3 0 .7-.2 1z"/></svg>
        0400 555 012
      </li>
      <li>
        <svg viewBox="0 0 24 24"><path d="M2 5h20v14H2z M3 6l9 7 9-7" fill="none" stroke="var(--ink-soft)" stroke-width="2"/></svg>
        marcus@ridgelineproperty.com
      </li>
      <li>
        <svg viewBox="0 0 24 24"><circle cx="12" cy="12" r="10"/><path d="M2 12h20M12 2c3 3 3 17 0 20M12 2c-3 3-3 17 0 20" stroke="var(--white)" stroke-width="1.4" fill="none"/></svg>
        www.RidgelineProperty.com
      </li>
    </ul>

    <address class="address">48 Harbour Lane<br>Kew VIC 3101</address>
  </section>

  <section class="card card-back" aria-label="Business card back">
    <svg class="stripes" viewBox="0 0 640 366" aria-hidden="true">
      <polygon points="0,70 330,0 360,0 0,76" fill="var(--stripe)" opacity="0.55"/>
      <polygon points="0,112 340,40 340,66 0,138" fill="var(--stripe)" opacity="0.75"/>
      <polygon points="0,160 300,96 300,122 0,186" fill="var(--stripe)" opacity="0.75"/>
      <polygon points="0,208 260,152 260,178 0,234" fill="var(--stripe)" opacity="0.75"/>
    </svg>
    <div class="brand">
      <div class="brand-name"><span class="brand-mark"></span>Ridgeline Property</div>
      <div class="brand-sub">Group</div>
    </div>
  </section>

</main>
</body>
</html>
```